Laser Tattoo Removal Business Cards

We are looking for a professional business card design for a laser tattoo removal business. Ideally looking for a black business card design. The name of the business is Lumen Ink Clearing. We place our cards at local tattoo shops so we ideally are looking for something trendy/edgy to draw both male and female clientele in.

Target Market(s)

Male/Female ages 18-60

Contact Information for Business Card

black background ideally.. hoping to stay within greys, whites and black

Font styles to use
Serif
Sans Serif

Colors
121212
a9a9a9
5c5c5c
f5f5f5
ffffff
7f7f7f
606060
848484
9d9d9d

Requirements
Must have
• Employee Info:
• Marisol Dunmore
• Chief Executive Offer
• m: 919.555.0143
• w: 919.555.0178
• f: 919.555.0192
• mdunmore@lumeninkclearing.com
• Address:
• 4185 Fenwick Pkwy, Suite 210
• Raleigh, NC 27617
• Website:
• www.lumeninkclearing.com
Nice to have
• Myabe business name on back or logo on back and employee info on the front

```html
<!DOCTYPE html>
<html lang="en">
<head>
<meta charset="utf-8">
<title>Lumen Ink Clearing – Business Card</title>
<link rel="stylesheet" href="https://fonts.googleapis.com/css2?family=Montserrat:wght@400;500;600&display=swap">
<style>
  :root {
    --backdrop: #3a3a3a;
    --card-white: #ffffff;
    --panel-dark: #2c2a2b;
    --ink: #121212;
    --text-light: #f5f5f5;
    --photo-light: #f5f5f5;
    --photo-pale: #d9d9d9;
    --photo-mid: #9d9d9d;
    --photo-grey: #7f7f7f;
    --photo-deep: #2a2a2a;
  }
  * { box-sizing: border-box; margin: 0; padding: 0; }
  html, body {
    width: 1200px; height: 960px; overflow: hidden;
    background: var(--backdrop);
    font-family: "Montserrat", Arial, sans-serif;
  }
  .canvas { position: relative; width: 1200px; height: 960px; }
  .card {
    position: absolute; left: 281px; width: 655px; height: 374px;
    border-radius: 18px; overflow: hidden; background: var(--card-white);
    box-shadow: 0 6px 18px rgba(0,0,0,.35);
  }
  .card--front { top: 80px; }
  .card--back { top: 506px; height: 375px; }

  .front__brand {
    position: absolute; left: 0; top: 0; width: 326px; height: 100%;
    display: flex; align-items: center; justify-content: center;
    padding-bottom: 20px;
  }
  .wordmark {
    font-weight: 500; color: var(--ink); letter-spacing: 0.1em;
    text-transform: uppercase; font-size: 20px; white-space: nowrap;
  }
  .front__info {
    position: absolute; left: 326px; top: 0; right: 0; height: 100%;
    background: var(--panel-dark); color: var(--text-light);
    padding: 63px 0 0 41px;
  }
  .person__name { font-size: 21px; font-weight: 600; letter-spacing: 0.01em; text-transform: uppercase; line-height: 26px; }
  .person__title { font-size: 16px; margin-top: 3px; font-weight: 400; line-height: 22px; }
  .address { font-size: 14px; line-height: 22px; margin-top: 20px; }
  .contacts { list-style: none; margin-top: 22px; font-size: 14px; }
  .contacts li { display: flex; align-items: center; height: 22px; white-space: nowrap; }
  .contacts svg { width: 11px; height: 11px; margin-right: 9px; fill: var(--text-light); flex: none; }

  .back__photo {
    position: absolute; left: 0; right: 0; bottom: 0; height: 255px;
    background:
      linear-gradient(to bottom, var(--card-white) 0%, rgba(255,255,255,0) 30%),
      radial-gradient(ellipse 32% 55% at 92% 88%, var(--photo-deep) 0%, rgba(42,42,42,0) 100%),
      radial-gradient(ellipse 30% 70% at 14% 80%, var(--photo-deep) 0%, rgba(42,42,42,.6) 45%, rgba(42,42,42,0) 100%),
      radial-gradient(ellipse 40% 45% at 60% 75%, var(--photo-pale) 0%, rgba(217,217,217,0) 100%),
      linear-gradient(to bottom, var(--photo-light) 0%, var(--photo-mid) 60%, var(--photo-grey) 100%);
  }
  .back__brand {
    position: absolute; right: 40px; top: 84px;
  }
</style>
</head>
<body>
<div class="canvas">
  <section class="card card--front">
    <div class="front__brand">
      <span class="wordmark">Lumen Ink Clearing</span>
    </div>
    <div class="front__info">
      <h1 class="person__name">Marisol Dunmore</h1>
      <p class="person__title">Chief Executive Offer</p>
      <p class="address">4185 Fenwick Pkwy, Suite 210<br>Raleigh, NC 27617</p>
      <ul class="contacts">
        <li><svg viewBox="0 0 12 12" aria-hidden="true"><path d="M3 0h6v12H3z M4 1v9h4V1z" fill-rule="evenodd"/></svg>919.555.0143</li>
        <li><svg viewBox="0 0 12 12" aria-hidden="true"><path d="M2.5 1l2 2-1 1.5c.8 1.6 2 2.8 3.5 3.5L8.5 7l2 2-1.5 2C5 10.5 1.5 7 1 2.5z"/></svg>919.555.0178</li>
        <li><svg viewBox="0 0 12 12" aria-hidden="true"><path d="M3 1h6v3H3z M1 5h10v5H9v-2H3v2H1z M4 9h4v2H4z"/></svg>919.555.0192</li>
        <li><svg viewBox="0 0 12 12" aria-hidden="true"><path d="M1 3h10v6H1z M1 3l5 3.5L11 3" stroke="var(--panel-dark)" stroke-width="0.8"/></svg>mdunmore@lumeninkclearing.com</li>
        <li><svg viewBox="0 0 12 12" aria-hidden="true"><circle cx="6" cy="6" r="5"/><path d="M1 6h10M6 1v10M6 1c-2.5 2.5-2.5 7.5 0 10M6 1c2.5 2.5 2.5 7.5 0 10" stroke="var(--panel-dark)" stroke-width="0.7" fill="none"/></svg>www.lumeninkclearing.com</li>
      </ul>
    </div>
  </section>

  <section class="card card--back">
    <div class="back__photo" role="img" aria-label="Photo of a technician in gloves performing laser tattoo removal on a client's hip tattoo, fading into white at the top"></div>
    <div class="back__brand"><span class="wordmark">Lumen Ink Clearing</span></div>
  </section>
</div>
</body>
</html>
```